FLOWx PI Planning Web App - Lean Agile at Scale - Distributed Big Room Planning Web & Touchscr...

We are the provider of the roadmapr app http://roadmapr-board.example which currently is a desktop application. We are now working to bring all the features to a web-app but we don’t have a catchy design yet. The roadmapr app is a visual collaboration tool for globally distributed teams and organization. Imagine a wall with lots of sticky notes on a flipchart hanging there – that’s basically our app just in a digital format. In general we want a light, modern, state of the art look and feel. Please take colorblind people into consideration when designing it.We are specifically looking for the following two design parts:- Design of the board structure- Sticky note designRequirements for the board structure- 16:9 ratio fixed- The board can be structured in 2 to 12 iterations + Risk Area and Objectives. Most common is 5 iterations + Risk Area and Objectives. Please go with the most common one but have in the back of your head that it needs to be compatible with 14 sections. Just for your imagination: in real life each of these areas on the board is one flip chart page.- Team Name: Somewhere on the board has to be the team name. It has to be easy to find and read.- In the iteration fields the user can set a velocity. That’s a simple numbers field. The load is calculated automatically and is just a number displayed on the board. There is an automatic visual indicator which should show with green or red colors if the teams are still in the plan. How this is brought to the attention is up to you.- Objectives & Stretch Objectives: The area with the Objectives is a list with text and a prioritization number attached to it. BV on the sketch stands for Business Value.Sticky Note design descriptionThe Sticky Note represents a physical sticky note or post-it note. When the user sees it he should instantly understand it as a sticky note and so for intuitively know what to do with it.Unselected sticky noteIf the sticky note is not selected it should be a simple sticky note sitting on the board.Following you find the things visible when the sticky note is not selected:- The sticky notes have a squared form factor- There is the text which is on the sticky note- In the upper right corner is a small sticky ID. Something like e.g. RT-4253.- Somewhere on the sticky note is also a number which should be easy to read. The numbers range from nothing over 0.5, 1, 2, 3, 5, 8, 13, 20, 40 up to 100.- Somewhere on the sticky needs to be a permanent text label. Not bigger than the rest of the text on the sticky note but easy to read.Selected sticky noteIf the user clicks on the sticky note once the following information needs to be displayed and he needs to be able to do the things listed and described below:- The sticky notes have a squared form factor- The user can write text on it- He can select different colors. These colors need to have a label so he knows what the function of these colors are.- By clicking a button he can add a flag to the sticky note- He can open a selection to choose the following number displayed on the sticky: 0.5, 1, 2, 3, 5, 8, 13, 20, 40, 100.- There is a delete sticky button. Place it where it makes sense from an intuitive stand point.- If he clicks the delete button, a short dialog appears on the sticky note: “Are you sure you want to delete this sticky note permanently? (It might delete an issue in your ALM tool)” He can confirm that by pressing “Delete” or “Cancel”.- In the upper right corner is a small sticky ID. Something like e.g. RT-4253.- Somewhere on or next to the sticky note needs to be a “sticky mirror” button as well as a “sticky move” button. Beside an optional icon for “mirror” and “move” there needs to be a naming tag so that everyone understands it right away.- It’s up to you to decide what’s the most intuitive way for the user.For better understanding also take a look at the rough sketch attached.

Font styles to use
Sans Serif

Requirements
Must have
• Color blind mode for different colored sticky notes

```html
<!DOCTYPE html>
<html lang="en">
<head>
<meta charset="utf-8">
<title>Team Board</title>
<link rel="stylesheet" href="https://fonts.googleapis.com/css2?family=Mulish:wght@200;300;400;600;700;800;900&display=swap">
<style>
:root{
  --gray-band:#8a8a8a;
  --band-text:#e4e4e4;
  --ink:#1b1b1b;
  --muted:#777;
  --line:#e3e3e3;
  --blue:#1a8fe3;
  --red:#e8474f;
  --yellow:#f5c800;
  --purple:#5b1a9e;
  --def:#cfcfcf;
  --note-default:#f6f6f6;
  --note-yellow:#fdf7d6;
  --note-purple:#e9e1f2;
  --note-risk:#fbe2e5;
  --risk-border:#f0a5ab;
  --iter3-bg:#f5f9fb;
  --iter5-bg:#fff6f6;
}
*{box-sizing:border-box;margin:0;padding:0}
html,body{width:814px;height:1200px;overflow:hidden;background:var(--gray-band)}
body{font-family:'Mulish',sans-serif;color:var(--ink)}
.stage{position:absolute;left:0;top:0;width:1576px;height:2324px;transform:scale(.5165);transform-origin:0 0;background:var(--gray-band)}
.band-title{position:absolute;left:0;width:1576px;text-align:center;color:var(--band-text);font-size:18px;font-weight:300;letter-spacing:.3px}
.board{position:absolute;left:0;width:1576px;height:887px;background:#fff}
.board--near{--note-default:#fff;--note-yellow:#fff;--note-purple:#fff;--note-risk:#fff;--risk-border:var(--red)}
.section{position:absolute;border-left:1px solid var(--line);border-top:1px solid var(--line)}
.section--iter3{background:var(--iter3-bg)}
.section--iter5{background:var(--iter5-bg)}
.ribbon{position:absolute;left:0;top:0;width:20px;height:28px;clip-path:polygon(0 0,100% 0,100% 100%,50% 80%,0 100%)}
.ribbon--blue{background:#cfe6f4}
.ribbon--pink{background:#f9d3d6}
.ribbon svg{position:absolute;left:4px;top:5px}

.team-name{position:absolute;left:16px;top:20px;font-size:34px;font-weight:200;line-height:36px;letter-spacing:.4px}
.obj-head{position:absolute;left:16px;display:flex;align-items:center;gap:6px;color:var(--blue);font-weight:900;font-size:19px;letter-spacing:.2px}
.obj-bv{position:absolute;right:16px;color:var(--blue);font-weight:900;font-size:16px}
.obj-item{position:absolute;left:16px;width:242px;font-size:12px;line-height:18px;padding-bottom:14px;border-bottom:1px solid var(--line)}
.obj-item b{position:absolute;right:0;top:0;font-size:13px;font-weight:800}
.obj-item span{display:block;width:200px}
.legend{position:absolute;left:16px;display:grid;grid-template-columns:129px 120px;row-gap:8px;font-size:11.5px}
.legend span{display:flex;align-items:center;gap:5px}
.dot{width:11px;height:11px;border-radius:50%;display:inline-block}
.tip{position:absolute;left:125px;background:#111;color:#fff;font-size:8px;font-weight:900;padding:5px 8px;border-radius:3px}
.tip::after{content:"";position:absolute;left:21px;bottom:-5px;border:5px solid transparent;border-bottom:0;border-top-color:#111}
.bg-label{position:absolute;left:16px;font-size:11px;font-weight:900;letter-spacing:.2px}
.slider{position:absolute;left:16px;width:242px;height:3px;background:#d6d6d6;border-radius:2px}
.slider__fill{position:absolute;left:0;top:0;height:3px;background:#444}
.slider__knob{position:absolute;top:-6px;width:8px;height:15px;border:1px solid #333;background:#fff;border-radius:4px}
.slider-ends{position:absolute;left:16px;width:242px;display:flex;justify-content:space-between;font-size:6px;font-weight:700}

.iter-head{position:absolute;left:32px;top:26px;display:flex;align-items:center;white-space:nowrap}
.iter-title{font-size:19px;font-weight:900;letter-spacing:.3px;margin-right:16px}
.metric{font-size:10px;font-weight:800;display:flex;align-items:center;gap:5px;margin-right:16px}
.metric__box{display:inline-block;width:31px;height:15px;border:1px solid #222;text-align:center;font-size:10px;font-weight:600;line-height:13px;font-style:normal}
.metric__load{display:inline-block;width:30px;border-bottom:1px solid #222;text-align:center;font-size:10px;font-weight:600;font-style:normal}
.risk-head{position:absolute;left:32px;top:22px;display:flex;align-items:center;gap:6px;color:var(--red);font-size:19px;font-weight:900}

.note{position:absolute;width:118px;height:117px;border:1px solid #d2d2d2;background:var(--note-default)}
.note--yellow{border-color:var(--yellow);background:var(--note-yellow)}
.note--purple{border-color:var(--purple);background:var(--note-purple)}
.note--risk{border-color:var(--risk-border);background:var(--note-risk)}
.note__fold{position:absolute;left:0;top:0;width:15px;height:15px;background:#d0d0d0;clip-path:polygon(100% 0,100% 100%,0 100%)}
.note--yellow .note__fold{background:var(--yellow)}
.note--purple .note__fold{background:var(--purple)}
.note--risk .note__fold{left:auto;right:0;background:var(--red);clip-path:polygon(0 0,100% 100%,0 100%)}
.note__flag{position:absolute;left:-2px;top:-2px}
.note__id{position:absolute;right:6px;top:5px;font-size:6.5px;font-weight:700}
.note__cat{position:absolute;left:19px;top:5px;font-size:5.5px;color:#aaa}
.note--yellow .note__cat{color:#c9ae4a}
.note--purple .note__cat{color:#a58fc2}
.note__text{position:absolute;left:6px;right:5px;top:24px;font-size:7.6px;line-height:10.8px;color:#333}
.note__label{position:absolute;left:6px;bottom:5px;font-size:5.3px;font-weight:600}
.note__num{position:absolute;right:6px;bottom:2px;font-size:12.5px;font-weight:300;color:#444}

.sel{position:absolute;width:177px;height:209px;background:#fff;border:1px solid #111;box-shadow:0 2px 6px rgba(0,0,0,.15);overflow:hidden}
.sel__cat{position:absolute;left:8px;top:7px;width:118px;height:17px;border-bottom:1px solid #444;font-size:8px;display:flex;align-items:center;gap:4px}
.sel__cat .dot{width:8px;height:8px;background:var(--def)}
.sel__cat svg{position:absolute;right:4px;top:6px}
.sel__id{position:absolute;right:8px;top:9px;font-size:6.5px;color:#999}
.sel__text{position:absolute;left:8px;right:8px;top:35px;font-size:12.3px;line-height:16px;color:#222}
.sel__controls{position:absolute;left:8px;right:8px;top:152px;display:flex;align-items:center;gap:5px}
.toggle{width:24px;height:8px;border:1px solid #111;border-radius:2px;position:relative;background:#fff}
.toggle::before{content:"ON";position:absolute;left:0;top:0;width:15px;height:6px;background:#111;color:#fff;font-size:4.5px;font-weight:900;text-align:center;line-height:6px}
.sel__num{margin-left:auto;font-size:19px;font-weight:300}
.toolbar{position:absolute;left:0;right:0;bottom:0;height:33px;background:#0c0c0c;display:flex}
.tool{flex:1;display:flex;flex-direction:column;align-items:center;justify-content:center;gap:3px;color:#fff;font-size:5.5px;font-weight:900;border-left:1px solid #666}
.tool:first-child{border-left:0}

.demo-label{position:absolute;top:2047px;width:178px;text-align:center;color:#d9d9d9;font-size:10px;font-weight:300}
.menu{position:absolute;left:8px;top:25px;width:118px;background:#fff;box-shadow:0 2px 6px rgba(0,0,0,.25);padding:5px 0}
.menu li{list-style:none;display:flex;align-items:center;gap:5px;font-size:7.5px;padding:4px 8px}
.menu .dot{width:8px;height:8px}
.menu .ring{width:8px;height:8px;border:1px solid #333;border-radius:50%}
.shade{position:absolute;inset:0;background:rgba(30,30,30,.86)}
.dialog-title{position:absolute;left:0;right:0;top:17px;text-align:center;color:#fff;font-size:9.5px;font-weight:900}
.field-label{position:absolute;left:10px;right:8px;top:42px;color:#fff;font-size:7.5px;padding-bottom:3px;border-bottom:1px solid #fff}
.picker{position:absolute;left:10px;top:70px;width:88px;height:86px;background:linear-gradient(to top,#000,transparent),linear-gradient(to right,#fff,#f8d905)}
.hue{position:absolute;left:105px;top:70px;width:7px;height:86px;background:linear-gradient(#f00,#ff0,#0f0,#0ff,#00f,#f0f,#f00)}
.swatch{position:absolute;left:119px;top:70px;width:46px;height:19px;background:#f8d905;border-radius:2px}
.rgb{position:absolute;left:119px;font-size:5.5px;color:#fff;display:flex;gap:4px;align-items:center}
.rgb i{font-style:normal;display:block;width:36px;height:10px;background:#111;padding-left:3px;line-height:10px}
.btn{position:absolute;height:17px;font-size:6.5px;font-weight:900;display:flex;align-items:center;justify-content:center;gap:3px}
.btn--ghost{border:1px solid #fff;color:#fff}
.btn--solid{background:#fff;color:#111}
.confirm{position:absolute;left:0;right:0;top:78px;text-align:center;color:#fff;font-size:9.5px;font-weight:800;line-height:13px}
</style>
</head>
<body>
<div class="stage">

<p class="band-title" style="top:54px">Sample view from a distance</p>

<section class="board" style="top:88px">
  <div class="section" style="left:0;top:0;width:275px;height:887px;border:0">
    <h1 class="team-name">The Team Name<br>Goes Here</h1>
    <div class="obj-head" style="top:134px"><svg width="27" height="27" viewBox="0 0 27 27"><circle cx="13" cy="14" r="11" fill="none" stroke="#1a8fe3" stroke-width="2"/><circle cx="13" cy="14" r="6.5" fill="none" stroke="#1a8fe3" stroke-width="2"/><circle cx="13" cy="14" r="2.2" fill="#1a8fe3"/><path d="M13 14 L24 3" stroke="#1a8fe3" stroke-width="2"/><path d="M21 2h4v4" fill="none" stroke="#1a8fe3" stroke-width="2"/></svg>OBJECTIVES</div>
    <div class="obj-bv" style="top:139px">BV</div>
    <div class="obj-item" style="top:175px"><span>Lorem ipsum dolor sit amet, consectetur adipiscing elit. Nullamv diam non felis varius dignisim eget.</span><b>10</b></div>
    <div class="obj-item" style="top:254px"><span>Curabitur sagittis tortor at erat ultricies, ac hendrerit justo iaculis.</span><b>8</b></div>
    <div class="obj-head" style="top:344px;font-size:17px">STRETCH OBJECTIVES</div>
    <div class="obj-item" style="top:381px"><span>Pellentesque, dolor tristique diam tortor augue fringilla arcu eros.</span><b>4</b></div>
    <div class="obj-item" style="top:442px"><span>Cras gravida scelerisque magna ultrices gregestas feugiat pharetra.</span><b>2</b></div>
    <div class="tip" style="top:724px">YELLOW</div>
    <div class="legend" style="top:750px">
      <span><i class="dot" style="background:var(--def)"></i>Default Category</span>
      <span><i class="dot" style="background:var(--yellow)"></i>Color Category 1</span>
      <span><i class="dot" style="background:var(--purple)"></i>Color Category 2</span>
      <span><i class="dot" style="background:var(--red)"></i>Risks</span>
    </div>
    <div class="bg-label" style="top:824px">STICKY NOTE BACKGROUND</div>
    <div class="slider" style="top:852px"><div class="slider__fill" style="width:32px"></div><div class="slider__knob" style="left:28px"></div></div>
    <div class="slider-ends" style="top:865px"><span>NONE</span><span>100%</span></div>
  </div>

  <div class="section" style="left:275px;top:0;width:434px;height:444px">
    <div class="iter-head"><span class="iter-title">ITERATION 1</span><span class="metric">Velocity <i class="metric__box">8</i></span><span class="metric">Load <i class="metric__load">6</i></span></div>
    <div class="note" style="left:32px;top:68px"><i class="note__fold"></i><span class="note__id">RT-4253</span><p class="note__text">Lorem ipsum dolor sit amet, consectetur adipiscing elit. Nullam vel diam non felis varius dignissim ege rabitur.</p><span class="note__label">Permanent Text Label</span><span class="note__num">20</span></div>
    <div class="note" style="left:32px;top:192px"><i class="note__fold"></i><span class="note__id">RT-4256</span><p class="note__text">Sed nec tincidunt velit, at consequat morbi vestibulum.</p><span class="note__label">Permanent Text Label</span><span class="note__num">8</span></div>
    <div class="note" style="left:280px;top:68px"><i class="note__fold"></i><span class="note__id">RT-4255</span><p class="note__text">Nam ullamcorper metus ut malesuada egestas. Vivamus erat, tellus vel vestibulum, eros at massa vitae.</p><span class="note__label">Permanent Text Label</span><span class="note__num">13</span></div>
    <div class="sel" style="left:157px;top:68px">
      <div class="sel__cat"><i class="dot"></i>Default Category<svg width="7" height="5" viewBox="0 0 7 5"><path d="M.5.5 3.5 3.5 6.5.5" fill="none" stroke="#333"/></svg></div>
      <span class="sel__id">RT-4254</span>
      <p class="sel__text">Cras gravida scelerisque magna ultrices gravida eget massa amet lectus justo.</p>
      <div class="sel__controls"><svg width="7" height="9" viewBox="0 0 7 9"><path d="M1 0v9M1 1h6l-2 2 2 2H1" fill="#111" stroke="#111"/></svg><span class="toggle"></span><span class="sel__num">100</span></div>
      <div class="toolbar">
        <div class="tool"><svg width="10" height="10" viewBox="0 0 10 10"><rect x="3" y="0" width="7" height="7" fill="#fff"/><rect x="0" y="3" width="7" height="7" fill="#fff" stroke="#0c0c0c"/></svg>DUPLICATE</div>
        <div class="tool"><svg width="11" height="11" viewBox="0 0 11 11"><path d="M5.5 0 3.5 2.5h4zM5.5 11l-2-2.5h4zM0 5.5l2.5-2v4zM11 5.5l-2.5-2v4zM5 2h1v7H5zM2 5h7v1H2z" fill="#fff"/></svg>MOVE</div>
        <div class="tool"><svg width="8" height="10" viewBox="0 0 8 10"><path d="M0 1h8v1H0zM3 0h2v1H3zM1 2.5h6V10H1z" fill="#fff"/></svg>DELETE</div>
      </div>
    </div>
  </div>

  <div class="section" style="left:709px;top:0;width:434px;height:444px">
    <div class="iter-head"><span class="iter-title">ITERATION 2</span><span class="metric">Velocity <i class="metric__box">20</i></span><span class="metric">Load <i class="metric__load">10</i></span></div>
    <div class="note note--yellow" style="left:32px;top:68px"><i class="note__fold"></i><svg class="note__flag" width="9" height="10" viewBox="0 0 9 10"><path d="M1 0v10M1 1h8L7 3.5 9 6H1" fill="#111" stroke="#111"/></svg><span class="note__cat">Color Category 1</span><span class="note__id">RT-4257</span><p class="note__text">In in augue id pellentesque condimentum in quis nulla fermentum sapien metus.</p><span class="note__label">Permanent Text Label</span><span class="note__num">0.5</span></div>
    <div class="note note--purple" style="left:157px;top:68px"><i class="note__fold"></i><span class="note__cat">Color Category 2</span><span class="note__id">RT-4258</span><p class="note__text">Phasellus eu tempor mauris. Etiam at ipsum nec libero imperdiet pharetra raesent finibus ante enim dictum.</p><span class="note__label">Permanent Text Label</span><span class="note__num">2</span></div>
  </div>

  <div class="section section--iter3" style="left:1143px;top:0;width:433px;height:444px">
    <div class="ribbon ribbon--blue"><svg width="12" height="12" viewBox="0 0 12 12"><circle cx="6" cy="6" r="4" fill="none" stroke="#fff" stroke-width="2.5" stroke-dasharray="2 1.2"/><circle cx="6" cy="6" r="1.5" fill="#fff"/></svg></div>
    <div class="iter-head"><span class="iter-title">ITERATION 3</span><span class="metric">Velocity <i class="metric__box">13</i></span><span class="metric">Load <i class="metric__load">2</i></span></div>
    <div class="note" style="left:32px;top:68px"><i class="note__fold"></i><span class="note__id">RT-4259</span><p class="note__text">Mauris sodales diam ultricis sollicitudin dictum finibus.</p><span class="note__label">Permanent Text Label</span><span class="note__num">40</span></div>
    <div class="note note--yellow" style="left:157px;top:68px"><i class="note__fold"></i><svg class="note__flag" width="9" height="10" viewBox="0 0 9 10"><path d="M1 0v10M1 1h8L7 3.5 9 6H1" fill="#111" stroke="#111"/></svg><span class="note__cat">Color Category 1</span><span class="note__id">RT-4263</span><p class="note__text">Etiam diam quam, tincidunt a consequat sed, commodo in nunc. Morbi ullamcorper odio eget nulla egestas.</p><span class="note__label">Permanent Text Label</span><span class="note__num">3</span></div>
    <div class="note note--purple" style="left:281px;top:68px"><i class="note__fold"></i><span class="note__cat">Color Category 2</span><span class="note__id">RT-4264</span><p class="note__text">Nulla placerat luctus sapien dapibus molestie curabitur malesuada felis pharetra.</p><span class="note__label">Permanent Text Label</span><span class="note__num">8</span></div>
  </div>

  <div class="section" style="left:275px;top:444px;width:434px;height:443px">
    <div class="iter-head"><span class="iter-title">ITERATION 4</span><span class="metric">Velocity <i class="metric__box"></i></span></div>
  </div>

  <div class="section section--iter5" style="left:709px;top:444px;width:434px;height:443px">
    <div class="ribbon ribbon--pink"><svg width="12" height="12" viewBox="0 0 12 12"><path d="M0 6q6-7 12 0-6 7-12 0z" fill="#fff"/><circle cx="6" cy="6" r="2" fill="#f9d3d6"/></svg></div>
    <div class="iter-head"><span class="iter-title">ITERATION 5</span><span class="metric">Velocity <i class="metric__box">5</i></span><span class="metric">Load <i class="metric__load">13</i></span></div>
    <div class="note" style="left:32px;top:68px"><i class="note__fold"></i><span class="note__id">RT-4260</span><p class="note__text">Aliquam dignissim ante sit amet consectetur vehicula. Vestibulum erat mauris, placerat tempor imperdiet.</p><span class="note__label">Permanent Text Label</span><span class="note__num">3</span></div>
    <div class="note" style="left:157px;top:68px"><i class="note__fold"></i><span class="note__id">RT-4261</span><p class="note__text">Curabitur vitae lacinia finibus nunc amet egestas.</p><span class="note__label">Permanent Text Label</span><span class="note__num">1</span></div>
    <div class="note" style="left:281px;top:68px"><i class="note__fold"></i><span class="note__id">RT-4262</span><p class="note__text">Donec pretium nibh vitae dolor vulputate pretium. uspendisse et purus pharetra, convallis quam vestibulum, aliquam lorem.</p><span class="note__label">Permanent Text Label</span><span class="note__num">0.5</span></div>
    <div class="note note--yellow" style="left:32px;top:192px"><i class="note__fold"></i><svg class="note__flag" width="9" height="10" viewBox="0 0 9 10"><path d="M1 0v10M1 1h8L7 3.5 9 6H1" fill="#111" stroke="#111"/></svg><span class="note__cat">Color Category 1</span><span class="note__id">RT-4265</span><p class="note__text">Pellentesque purus nibh, tempus quis tellus a, ultricies congue enim. Ut arcu mauris, hendrerit nibh vitae, fermentum mattis sapien.</p><span class="note__label">Permanent Text Label</span><span class="note__num">20</span></div>
    <div class="note note--purple" style="left:157px;top:192px"><i class="note__fold"></i><span class="note__cat">Color Category 2</span><span class="note__id">RT-4266</span><p class="note__text">Mauris condimentum tempo urna rhoncus sit amet consectet pulvinar molestie.</p><span class="note__label">Permanent Text Label</span><span class="note__num">40</span></div>
  </div>

  <div class="section" style="left:1143px;top:444px;width:433px;height:443px">
    <div class="risk-head"><svg width="26" height="23" viewBox="0 0 26 23"><path d="M13 1 25 22H1z" fill="none" stroke="#e8474f" stroke-width="1.6"/><path d="M13 8v7" stroke="#e8474f" stroke-width="2"/><circle cx="13" cy="18" r="1.2" fill="#e8474f"/></svg>RISKS</div>
    <div class="note note--risk" style="left:32px;top:68px"><i class="note__fold"></i><p class="note__text">Integer enim enim, efficitur a est pharetra lacinia mass fusce dictum velit gravida.</p></div>
    <div class="note note--risk" style="left:157px;top:68px"><i class="note__fold"></i><p class="note__text">Suspendisse et purus pharet convallis vestibulum, aliqua lorem. Nullam auctor tortor blandit leo mattis blandit estibulum ante ipsum primis.</p></div>
  </div>
</section>

<p class="band-title" style="top:1059px">Sample view when people are near the board</p>

<section class="board board--near" style="top:1093px">
  <div class="section" style="left:0;top:0;width:275px;height:887px;border:0">
    <h1 class="team-name">The Team Name<br>Goes Here</h1>
    <div class="obj-head" style="top:134px"><svg width="27" height="27" viewBox="0 0 27 27"><circle cx="13" cy="14" r="11" fill="none" stroke="#1a8fe3" stroke-width="2"/><circle cx="13" cy="14" r="6.5" fill="none" stroke="#1a8fe3" stroke-width="2"/><circle cx="13" cy="14" r="2.2" fill="#1a8fe3"/><path d="M13 14 L24 3" stroke="#1a8fe3" stroke-width="2"/><path d="M21 2h4v4" fill="none" stroke="#1a8fe3" stroke-width="2"/></svg>OBJECTIVES</div>
    <div class="obj-bv" style="top:139px">BV</div>
    <div class="obj-item" style="top:175px"><span>Lorem ipsum dolor sit amet, consectetur adipiscing elit. Nullamv diam non felis varius dignisim eget.</span><b>10</b></div>
    <div class="obj-item" style="top:254px"><span>Curabitur sagittis tortor at erat ultricies, ac hendrerit justo iaculis.</span><b>8</b></div>
    <div class="obj-head" style="top:344px;font-size:17px">STRETCH OBJECTIVES</div>
    <div class="obj-item" style="top:381px"><span>Pellentesque, dolor tristique diam tortor augue fringilla arcu eros.</span><b>4</b></div>
    <div class="obj-item" style="top:442px"><span>Cras gravida scelerisque magna ultrices gregestas feugiat pharetra.</span><b>2</b></div>
    <div class="tip" style="top:724px">YELLOW</div>
    <div class="legend" style="top:750px">
      <span><i class="dot" style="background:var(--def)"></i>Default Category</span>
      <span><i class="dot" style="background:var(--yellow)"></i>Color Category 1</span>
      <span><i class="dot" style="background:var(--purple)"></i>Color Category 2</span>
      <span><i class="dot" style="background:var(--red)"></i>Risks</span>
    </div>
    <div class="bg-label" style="top:824px">STICKY NOTE BACKGROUND</div>
    <div class="slider" style="top:852px"><div class="slider__knob" style="left:0"></div></div>
    <div class="slider-ends" style="top:865px"><span>NONE</span><span>100%</span></div>
  </div>

  <div class="section" style="left:275px;top:0;width:434px;height:444px">
    <div class="iter-head"><span class="iter-title">ITERATION 1</span><span class="metric">Velocity <i class="metric__box">8</i></span><span class="metric">Load <i class="metric__load">6</i></span></div>
    <div class="note" style="left:32px;top:68px"><i class="note__fold"></i><span class="note__id">RT-4253</span><p class="note__text">Lorem ipsum dolor sit amet, consectetur adipiscing elit. Nullam vel diam non felis varius dignissim ege rabitur.</p><span class="note__label">Permanent Text Label</span><span class="note__num">20</span></div>
    <div class="note" style="left:32px;top:192px"><i class="note__fold"></i><span class="note__id">RT-4256</span><p class="note__text">Sed nec tincidunt velit, at consequat morbi vestibulum.</p><span class="note__label">Permanent Text Label</span><span class="note__num">8</span></div>
    <div class="note" style="left:280px;top:68px"><i class="note__fold"></i><span class="note__id">RT-4255</span><p class="note__text">Nam ullamcorper metus ut malesuada egestas. Vivamus erat, tellus vel vestibulum, eros at massa vitae.</p><span class="note__label">Permanent Text Label</span><span class="note__num">13</span></div>
    <div class="sel" style="left:157px;top:68px">
      <div class="sel__cat"><i class="dot"></i>Default Category<svg width="7" height="5" viewBox="0 0 7 5"><path d="M.5.5 3.5 3.5 6.5.5" fill="none" stroke="#333"/></svg></div>
      <span class="sel__id">RT-4254</span>
      <p class="sel__text">Cras gravida scelerisque magna ultrices gravida eget massa amet lectus justo.</p>
      <div class="sel__controls"><svg width="7" height="9" viewBox="0 0 7 9"><path d="M1 0v9M1 1h6l-2 2 2 2H1" fill="#111" stroke="#111"/></svg><span class="toggle"></span><span class="sel__num">100</span></div>
      <div class="toolbar">
        <div class="tool"><svg width="10" height="10" viewBox="0 0 10 10"><rect x="3" y="0" width="7" height="7" fill="#fff"/><rect x="0" y="3" width="7" height="7" fill="#fff" stroke="#0c0c0c"/></svg>DUPLICATE</div>
        <div class="tool"><svg width="11" height="11" viewBox="0 0 11 11"><path d="M5.5 0 3.5 2.5h4zM5.5 11l-2-2.5h4zM0 5.5l2.5-2v4zM11 5.5l-2.5-2v4zM5 2h1v7H5zM2 5h7v1H2z" fill="#fff"/></svg>MOVE</div>
        <div class="tool"><svg width="8" height="10" viewBox="0 0 8 10"><path d="M0 1h8v1H0zM3 0h2v1H3zM1 2.5h6V10H1z" fill="#fff"/></svg>DELETE</div>
      </div>
    </div>
  </div>

  <div class="section" style="left:709px;top:0;width:434px;height:444px">
    <div class="iter-head"><span class="iter-title">ITERATION 2</span><span class="metric">Velocity <i class="metric__box">20</i></span><span class="metric">Load <i class="metric__load">10</i></span></div>
    <div class="note note--yellow" style="left:32px;top:68px"><i class="note__fold"></i><svg class="note__flag" width="9" height="10" viewBox="0 0 9 10"><path d="M1 0v10M1 1h8L7 3.5 9 6H1" fill="#111" stroke="#111"/></svg><span class="note__cat">Color Category 1</span><span class="note__id">RT-4257</span><p class="note__text">In in augue id pellentesque condimentum in quis nulla fermentum sapien metus.</p><span class="note__label">Permanent Text Label</span><span class="note__num">0.5</span></div>
    <div class="note note--purple" style="left:157px;top:68px"><i class="note__fold"></i><span class="note__cat">Color Category 2</span><span class="note__id">RT-4258</span><p class="note__text">Phasellus eu tempor mauris. Etiam at ipsum nec libero imperdiet pharetra raesent finibus ante enim dictum.</p><span class="note__label">Permanent Text Label</span><span class="note__num">2</span></div>
  </div>

  <div class="section section--iter3" style="left:1143px;top:0;width:433px;height:444px">
    <div class="ribbon ribbon--blue"><svg width="12" height="12" viewBox="0 0 12 12"><circle cx="6" cy="6" r="4" fill="none" stroke="#fff" stroke-width="2.5" stroke-dasharray="2 1.2"/><circle cx="6" cy="6" r="1.5" fill="#fff"/></svg></div>
    <div class="iter-head"><span class="iter-title">ITERATION 3</span><span class="metric">Velocity <i class="metric__box">13</i></span><span class="metric">Load <i class="metric__load">2</i></span></div>
    <div class="note" style="left:32px;top:68px"><i class="note__fold"></i><span class="note__id">RT-4259</span><p class="note__text">Mauris sodales diam ultricis sollicitudin dictum finibus.</p><span class="note__label">Permanent Text Label</span><span class="note__num">40</span></div>
    <div class="note note--yellow" style="left:157px;top:68px"><i class="note__fold"></i><svg class="note__flag" width="9" height="10" viewBox="0 0 9 10"><path d="M1 0v10M1 1h8L7 3.5 9 6H1" fill="#111" stroke="#111"/></svg><span class="note__cat">Color Category 1</span><span class="note__id">RT-4263</span><p class="note__text">Etiam diam quam, tincidunt a consequat sed, commodo in nunc. Morbi ullamcorper odio eget nulla egestas.</p><span class="note__label">Permanent Text Label</span><span class="note__num">3</span></div>
    <div class="note note--purple" style="left:281px;top:68px"><i class="note__fold"></i><span class="note__cat">Color Category 2</span><span class="note__id">RT-4264</span><p class="note__text">Nulla placerat luctus sapien dapibus molestie curabitur malesuada felis pharetra.</p><span class="note__label">Permanent Text Label</span><span class="note__num">8</span></div>
  </div>

  <div class="section" style="left:275px;top:444px;width:434px;height:443px">
    <div class="iter-head"><span class="iter-title">ITERATION 4</span><span class="metric">Velocity <i class="metric__box"></i></span></div>
  </div>

  <div class="section section--iter5" style="left:709px;top:444px;width:434px;height:443px">
    <div class="ribbon ribbon--pink"><svg width="12" height="12" viewBox="0 0 12 12"><path d="M0 6q6-7 12 0-6 7-12 0z" fill="#fff"/><circle cx="6" cy="6" r="2" fill="#f9d3d6"/></svg></div>
    <div class="iter-head"><span class="iter-title">ITERATION 5</span><span class="metric">Velocity <i class="metric__box">5</i></span><span class="metric">Load <i class="metric__load">13</i></span></div>
    <div class="note" style="left:32px;top:68px"><i class="note__fold"></i><span class="note__id">RT-4260</span><p class="note__text">Aliquam dignissim ante sit amet consectetur vehicula. Vestibulum erat mauris, placerat tempor imperdiet.</p><span class="note__label">Permanent Text Label</span><span class="note__num">3</span></div>
    <div class="note" style="left:157px;top:68px"><i class="note__fold"></i><span class="note__id">RT-4261</span><p class="note__text">Curabitur vitae lacinia finibus nunc amet egestas.</p><span class="note__label">Permanent Text Label</span><span class="note__num">1</span></div>
    <div class="note" style="left:281px;top:68px"><i class="note__fold"></i><span class="note__id">RT-4262</span><p class="note__text">Donec pretium nibh vitae dolor vulputate pretium. uspendisse et purus pharetra, convallis quam vestibulum, aliquam lorem.</p><span class="note__label">Permanent Text Label</span><span class="note__num">0.5</span></div>
    <div class="note note--yellow" style="left:32px;top:192px"><i class="note__fold"></i><svg class="note__flag" width="9" height="10" viewBox="0 0 9 10"><path d="M1 0v10M1 1h8L7 3.5 9 6H1" fill="#111" stroke="#111"/></svg><span class="note__cat">Color Category 1</span><span class="note__id">RT-4265</span><p class="note__text">Pellentesque purus nibh, tempus quis tellus a, ultricies congue enim. Ut arcu mauris, hendrerit nibh vitae, fermentum mattis sapien.</p><span class="note__label">Permanent Text Label</span><span class="note__num">20</span></div>
    <div class="note note--purple" style="left:157px;top:192px"><i class="note__fold"></i><span class="note__cat">Color Category 2</span><span class="note__id">RT-4266</span><p class="note__text">Mauris condimentum tempo urna rhoncus sit amet consectet pulvinar molestie.</p><span class="note__label">Permanent Text Label</span><span class="note__num">40</span></div>
  </div>

  <div class="section" style="left:1143px;top:444px;width:433px;height:443px">
    <div class="risk-head"><svg width="26" height="23" viewBox="0 0 26 23"><path d="M13 1 25 22H1z" fill="none" stroke="#e8474f" stroke-width="1.6"/><path d="M13 8v7" stroke="#e8474f" stroke-width="2"/><circle cx="13" cy="18" r="1.2" fill="#e8474f"/></svg>RISKS</div>
    <div class="note note--risk" style="left:32px;top:68px"><i class="note__fold"></i><p class="note__text">Integer enim enim, efficitur a est pharetra lacinia mass fusce dictum velit gravida.</p></div>
    <div class="note note--risk" style="left:157px;top:68px"><i class="note__fold"></i><p class="note__text">Suspendisse et purus pharet convallis vestibulum, aliqua lorem. Nullam auctor tortor blandit leo mattis blandit estibulum ante ipsum primis.</p></div>
  </div>
</section>

<p class="demo-label" style="left:355px">Selected sticky note</p>
<p class="demo-label" style="left:556px">Select a category/color.</p>
<p class="demo-label" style="left:757px">Create a new category</p>
<p class="demo-label" style="left:1033px">Delete the sticky note</p>

<div class="sel" style="left:356px;top:2068px">
  <div class="sel__cat"><i class="dot"></i>Default Category<svg width="7" height="5" viewBox="0 0 7 5"><path d="M.5.5 3.5 3.5 6.5.5" fill="none" stroke="#333"/></svg></div>
  <span class="sel__id">RT-4254</span>
  <p class="sel__text">Cras gravida scelerisque magna ultrices gravida eget massa amet lectus justo.</p>
  <div class="sel__controls"><svg width="7" height="9" viewBox="0 0 7 9"><path d="M1 0v9M1 1h6l-2 2 2 2H1" fill="#111" stroke="#111"/></svg><span class="toggle"></span><span class="sel__num">100</span></div>
  <div class="toolbar">
    <div class="tool"><svg width="10" height="10" viewBox="0 0 10 10"><rect x="3" y="0" width="7" height="7" fill="#fff"/><rect x="0" y="3" width="7" height="7" fill="#fff" stroke="#0c0c0c"/></svg>DUPLICATE</div>
    <div class="tool"><svg width="11" height="11" viewBox="0 0 11 11"><path d="M5.5 0 3.5 2.5h4zM5.5 11l-2-2.5h4zM0 5.5l2.5-2v4zM11 5.5l-2.5-2v4zM5 2h1v7H5zM2 5h7v1H2z" fill="#fff"/></svg>MOVE</div>
    <div class="tool"><svg width="8" height="10" viewBox="0 0 8 10"><path d="M0 1h8v1H0zM3 0h2v1H3zM1 2.5h6V10H1z" fill="#fff"/></svg>DELETE</div>
  </div>
</div>

<div class="sel" style="left:557px;top:2068px">
  <div class="sel__cat"><i class="dot"></i>Default Category<svg width="7" height="5" viewBox="0 0 7 5"><path d="M.5.5 3.5 3.5 6.5.5" fill="none" stroke="#333"/></svg></div>
  <span class="sel__id">RT-4254</span>
  <p class="sel__text">Cras gravida scelerisque magna ultrices gravida eget massa amet lectus justo.</p>
  <ul class="menu">
    <li><i class="dot" style="background:var(--def)"></i>Default Category</li>
    <li><i class="dot" style="background:var(--yellow)"></i>Color Category 1</li>
    <li><i class="dot" style="background:var(--purple)"></i>Color Category 2</li>
    <li><i class="ring"></i>Create a New Category</li>
  </ul>
  <div class="sel__controls"><svg width="7" height="9" viewBox="0 0 7 9"><path d="M1 0v9M1 1h6l-2 2 2 2H1" fill="#111" stroke="#111"/></svg><span class="toggle"></span><span class="sel__num">100</span></div>
  <div class="toolbar">
    <div class="tool"><svg width="10" height="10" viewBox="0 0 10 10"><rect x="3" y="0" width="7" height="7" fill="#fff"/><rect x="0" y="3" width="7" height="7" fill="#fff" stroke="#0c0c0c"/></svg>DUPLICATE</div>
    <div class="tool"><svg width="11" height="11" viewBox="0 0 11 11"><path d="M5.5 0 3.5 2.5h4zM5.5 11l-2-2.5h4zM0 5.5l2.5-2v4zM11 5.5l-2.5-2v4zM5 2h1v7H5zM2 5h7v1H2z" fill="#fff"/></svg>MOVE</div>
    <div class="tool"><svg width="8" height="10" viewBox="0 0 8 10"><path d="M0 1h8v1H0zM3 0h2v1H3zM1 2.5h6V10H1z" fill="#fff"/></svg>DELETE</div>
  </div>
</div>

<div class="sel" style="left:758px;top:2068px">
  <div class="sel__cat"><i class="dot"></i>Default Category</div>
  <p class="sel__text">Cras gravida scelerisque magna ultrices gravida eget massa amet lectus justo.</p>
  <div class="sel__controls"><span class="sel__num">100</span></div>
  <div class="toolbar"><div class="tool">DUPLICATE</div><div class="tool">MOVE</div><div class="tool">DELETE</div></div>
  <div class="shade">
    <p class="dialog-title">CREATE A CATEGORY</p>
    <p class="field-label">Category Name</p>
    <div class="picker"></div>
    <div class="hue"></div>
    <div class="swatch"></div>
    <div class="rgb" style="top:98px">R <i>248</i></div>
    <div class="rgb" style="top:112px">G <i>217</i></div>
    <div class="rgb" style="top:126px">B <i>5</i></div>
    <div class="rgb" style="top:144px;left:119px"><i style="width:46px">#f8d905</i></div>
    <div class="btn btn--ghost" style="left:28px;top:174px;width:58px">CANCEL</div>
    <div class="btn btn--solid" style="left:90px;top:174px;width:58px">▦ CREATE</div>
  </div>
</div>

<div class="sel" style="left:1033px;top:2068px">
  <div class="sel__cat"><i class="dot"></i>Default Category</div>
  <span class="sel__id">RT-4254</span>
  <p class="sel__text">Cras gravida scelerisque magna ultrices gravida eget massa amet lectus justo.</p>
  <div class="sel__controls"><span class="sel__num">100</span></div>
  <div class="toolbar"><div class="tool">DUPLICATE</div><div class="tool">MOVE</div><div class="tool">DELETE</div></div>
  <div class="shade">
    <p class="confirm">Are you sure you want to delete<br>this sticky note permanently?</p>
    <div class="btn btn--ghost" style="left:28px;top:113px;width:58px">CANCEL</div>
    <div class="btn btn--solid" style="left:91px;top:113px;width:58px"><svg width="6" height="8" viewBox="0 0 8 10"><path d="M0 1h8v1H0zM3 0h2v1H3zM1 2.5h6V10H1z" fill="#111"/></svg>DELETE</div>
  </div>
</div>

</div>
</body>
</html>
```